Vorlanda.com

Looking for a Graphic Designer/Web Designer to make a really modern/clean "skin" for our new Fitness website. This 'skin' will be used for the border/frame of all pages of the site.

Background:
Vorlanda is a company that is solely dedicated to providing personal trainers with a all-in-one suite of services to help manager, increase, and support their clients.

For a small monthly fee, personal trainers will have the ability to manage clients, schedule sessions, take payments, provide education, monitor their progress, track their results, and more.

What we are looking for:
Someone to create the graphics/banners for the page, help with fonts, size of fonts, spacing between elements, what borders, their colors.

The main page needs to focus on allowing the user to select whether they are a 'trainer' or a client. From their the page will open up to two difference experiences.

Personal Trainer Experience:
Personal Trainer Main page will show a sales section to offer the product and services. Once a trainer signs up for our service, they will log into a dashboard that will have several icons that lead to difference functions of the site. We will need help with placement of the various fields/data to make it visually appealing and provide a friendly user experience.

The client Experience: They will be directed to a client log-in page. Once logged in, they will be provided with a similar dashboard menu that provides them various options as well. We will need help with organizing the fields/data to make it visually appealing and provide a friend user experience.

This will be a great experience for both the designer and for us. Once the "skin" is created, it's a matter of making the rest visually appealing.

The icons being used for the 'dashboard menu':
http://plimvectorbay.com/fitness-icons-7312-vector-clipart.html

Any questions, please feel free to ask.

Target Market(s)

Our target market are personal trainers both seasoned and new.

Industry/Entity Type

Education

Requirements
Must have
• Must have a modern, upbeat look.
The main page for trainers needs to be professional and really highlight our services (selling page).
should have the option to link to the following services to see more about what you get:
Exercise, Nutrition, Supplementation, Documentation, Scheduling and Email, Payment process, Marketing
Nice to have
• Here are pages to some of the sites we liked (visually):
1. https://www.zorvix.com/ (really like the look of zorvxi)
2. http://pelodrasket.com/
3. http://www.brightmoldworks.com/gallery/tarn/
4. https://www.zorvix.com/
5 https://wavelorin.com/
5. http://www.plendrix.com/
6. http://www.tesvor.com/
7. http://www.florimenta.pl/
Should not have
• Here are some of our competitors:
www.gripstaveonline.com
www.oxlearnhub.com
www.lobrikdesk.com

```html
<!DOCTYPE html>
<html lang="en">
<head>
<meta charset="utf-8">
<title>Vorlanda – Personal Training Suite</title>
<link rel="stylesheet" href="https://fonts.googleapis.com/css2?family=Open+Sans:wght@400;600;700&display=swap">
<style>
  :root {
    --brand-green: #078040;
    --hero-green: #2e9a5e;
    --ink: #111111;
    --text-grey: #666666;
    --nav-grey: #e8e8e8;
    --nav-text: #333333;
    --footer-bg: #fafafa;
    --footer-line: #e2e2e2;
    --logo-faint: #c9c9c9;
    --white: #ffffff;
  }
  * { box-sizing: border-box; margin: 0; padding: 0; }
  html, body { width: 1200px; height: 652px; overflow: hidden; background: var(--white); }
  body { font-family: "Open Sans", Arial, sans-serif; color: var(--ink); }

  .page { position: relative; width: 1200px; height: 652px; overflow: hidden; border-top: 3px solid var(--brand-green); }

  /* Header */
  .site-header { position: absolute; top: 0; left: 0; width: 1200px; height: 84px; }
  .brand { position: absolute; left: 180px; top: 10px; }
  .brand-name { font-size: 50px; font-weight: 700; color: var(--ink); letter-spacing: -1px; line-height: 1; }
  .contact-phone { position: absolute; right: 180px; top: 16px; display: flex; align-items: center; gap: 6px; color: var(--brand-green); font-weight: 600; font-size: 15px; }
  .follow { position: absolute; right: 180px; top: 49px; display: flex; align-items: center; gap: 4px; font-size: 11px; color: var(--ink); }
  .follow-label { margin-right: 6px; }
  .social-box { width: 19px; height: 19px; background: var(--hero-green); }

  /* Navigation */
  .main-nav { position: absolute; top: 84px; left: 0; width: 1200px; height: 47px; background: var(--nav-grey); }
  .main-nav ul { list-style: none; position: relative; height: 100%; }
  .main-nav li { position: absolute; top: 0; height: 47px; line-height: 47px; font-size: 14px; color: var(--nav-text); }
  .main-nav li.is-active { background: var(--brand-green); color: var(--white); padding: 0 18px; }

  /* Hero */
  .hero { position: absolute; top: 137px; left: 0; width: 1023px; height: 323px; background: var(--hero-green); }
  .hero-shadow { position: absolute; top: 452px; left: 270px; width: 670px; height: 14px; background: radial-gradient(ellipse at center top, rgba(0,0,0,0.22), rgba(0,0,0,0) 70%); }
  .hero-photo { position: absolute; inset: 0; }
  .hero-offer { position: absolute; left: 206px; top: 50px; }
  .offer-amount { font-size: 48px; font-weight: 700; color: var(--white); line-height: 1; }
  .offer-title { margin-top: 20px; font-size: 34px; font-weight: 400; color: var(--ink); line-height: 41px; }
  .audience-choice { position: absolute; left: 205px; top: 228px; display: flex; gap: 8px; }
  .choice { display: block; height: 34px; line-height: 32px; font-size: 17px; text-decoration: none; border-bottom: 2px solid #9bb9a6; width: 104px; text-align: center; }
  .choice-trainer { background: var(--ink); color: var(--white); }
  .choice-client { background: var(--white); color: var(--brand-green); font-weight: 700; }

  /* Welcome */
  .welcome { position: absolute; top: 460px; left: 0; width: 1200px; height: 124px; }
  .welcome-title { position: absolute; left: 181px; top: 53px; font-size: 22px; font-weight: 700; color: var(--brand-green); }
  .welcome-divider { position: absolute; left: 436px; top: 37px; width: 3px; height: 69px; background: linear-gradient(to right, rgba(0,0,0,0.12), rgba(0,0,0,0)); }
  .welcome-text { position: absolute; left: 468px; top: 45px; width: 548px; font-size: 11px; line-height: 13.5px; color: var(--text-grey); }

  /* Footer */
  .site-footer { position: absolute; top: 584px; left: 0; width: 1200px; height: 68px; background: var(--footer-bg); border-top: 1px solid var(--footer-line); }
  .copyright { position: absolute; left: 181px; top: 27px; font-size: 11px; color: var(--text-grey); }
  .footer-brand { position: absolute; right: 180px; top: 14px; font-size: 38px; font-weight: 700; color: var(--logo-faint); line-height: 1; letter-spacing: -1px; }
</style>
</head>
<body>
<div class="page">

  <header class="site-header">
    <div class="brand">
      <span class="brand-name">Vorlanda</span>
    </div>
    <div class="contact-phone">
      <svg width="10" height="17" viewBox="0 0 10 17" aria-hidden="true">
        <rect x="1" y="1" width="8" height="15" rx="1.5" fill="none" stroke="#111" stroke-width="1.5"/>
        <line x1="3.5" y1="13.5" x2="6.5" y2="13.5" stroke="#111" stroke-width="1.2"/>
      </svg>
      <span>+48 612 309 847</span>
    </div>
    <div class="follow">
      <span class="follow-label">FOLLOW US:</span>
      <span class="social-box" role="img" aria-label="Social network link"></span>
      <span class="social-box" role="img" aria-label="Social network link"></span>
      <span class="social-box" role="img" aria-label="Social network link"></span>
    </div>
  </header>

  <nav class="main-nav">
    <ul>
      <li class="is-active" style="left:180px">HOME</li>
      <li style="left:273px">SERVICES</li>
      <li style="left:365px">FACILITIES</li>
      <li style="left:464px">CLIENTS</li>
      <li style="left:549px">TRAINERS</li>
      <li style="left:645px">BLOGS</li>
      <li style="left:722px">CLASSES</li>
      <li style="left:809px">CONTACT</li>
    </ul>
  </nav>

  <div class="hero-shadow"></div>
  <section class="hero">
    <svg class="hero-photo" width="1023" height="323" viewBox="0 0 1023 323" role="img" aria-label="Photo of a personal trainer coaching a client at a gym machine">
      <defs>
        <linearGradient id="gymTones" x1="0" y1="0" x2="1" y2="1">
          <stop offset="0" stop-color="#d9dcdb"/>
          <stop offset="0.5" stop-color="#a9aeac"/>
          <stop offset="1" stop-color="#4a4a4a"/>
        </linearGradient>
      </defs>
      <polygon points="694,0 1023,0 1023,323 476,323" fill="url(#gymTones)"/>
    </svg>
    <div class="hero-offer">
      <p class="offer-amount">2 FREE</p>
      <h1 class="offer-title">PERSONAL TRAINING<br>SESSIONS</h1>
    </div>
    <div class="audience-choice">
      <a class="choice choice-trainer" href="#">TRAINER</a>
      <a class="choice choice-client" href="#">CLIENTS</a>
    </div>
  </section>

  <section class="welcome">
    <h2 class="welcome-title">Welcome To Vorlanda</h2>
    <div class="welcome-divider"></div>
    <p class="welcome-text">Lorem Ipsum is that it has a more-or-less normal distribution of letters, as opposed to using 'Content here, content here', making it look like readable English. Many desktop publishing packages and web page editors now use Lorem Ipsum as their default model text, and a search for 'lorem ipsum' will uncover many web sites still in their infancy</p>
  </section>

  <footer class="site-footer">
    <p class="copyright">©2013 Vorlanda.All right Reserved</p>
    <div class="footer-brand">Vorlanda</div>
  </footer>

</div>
</body>
</html>
```